ONE PAGE WEB DESIGN NEEDED for Finance Company

We need a web design (ONE PAGE DESIGN ONLY) for a new finance website called Brightwell Lending. Brightwell Lending helps customers get the right loan, whether its a home loan, investment loan, business loan etc.

You are required to come up with just the homepage design. Professionalism and quality is the key factors in the successful design.

Here are a few design questions to help you out:

-
What information should be used on the page?
Ive provided a document which outlines all the information needed to put on homepage (attached to the brief - called brightwell_page_info). Also see the Must Have section below on this brief.

-
What links should appear in the navigation/footer?:
The navigation should provide links to the following pages (NOTE: services link has subcategories):
1 Homepage
2 Services
- Home loans
- Investment loans
- Refinancing loans
- Business loans
3 About Us
4 FAQ
5 Contact Us

-
What colors should be used in the design?
Our company colors - Cyan: #2EADE3, Blue: #004B70, White. Feel free to submit designs with slight variations if you feel it improves the design.

-
What should the layout of the page be?
This is up to you to come up with - we are open to different layouts for the page design (as long as they capture the information effectively and making it easy to understand).

Target Market(s)

Potential Home owners, Families and Business Owners

Industry/Entity Type

Business

Requirements
Must have
• - Must contain our logo (attached as PNG and Illustrator file)
- Winning designer must supply a Photoshop file (PSD) that will allow us.
Nice to have
• - Should include photos/images of families, professional groups, tradespeople etc (you can use stock photos from PixQuarry and I will purchase them once you are selected as the winning design)
- Link to a loan calculator somewhere on front page with a button 'Find out how much you could borrow' (or maybe even try adding a loan calculator to the homepage if you think this would look good)
- Page should have a main headline "Finding the right loan for you" or "Brightwell Lending finds the right loan for our customers."
- Must include Accreditation logos somewhere on the homepage (will try and supply these soon)
Should not have
• - Poor quality designs will not be considered
- Do not use clipart

```html
<!DOCTYPE html>
<html lang="en">
<head>
<meta charset="utf-8">
<title>Brightwell Lending – Home</title>
<link rel="stylesheet" href="https://fonts.googleapis.com/css2?family=Arimo:wght@400;700&family=Roboto+Condensed:wght@300;400&display=swap">
<style>
:root{
  --cyan:#2EADE3;
  --blue:#004B70;
  --ink:#222222;
  --white:#ffffff;
  --rule:#2EADE3;
  --badge:#d8d8d8;
}
*{box-sizing:border-box;margin:0;padding:0}
html,body{width:1200px;height:1200px;overflow:hidden;background:var(--white);font-family:"Arimo",Arial,sans-serif;color:var(--ink)}
.page{position:relative;width:1200px;height:1200px}
a{text-decoration:none;color:inherit}

.site-header{position:absolute;left:0;top:0;width:1200px;height:80px;background:var(--white)}
.brand{position:absolute;left:130px;top:51px;display:flex;align-items:center;gap:7px;height:20px}
.brand-mark{width:10px;height:10px;background:var(--cyan)}
.brand-name{font-size:16px;font-weight:400;color:var(--cyan);letter-spacing:-0.3px;white-space:nowrap;line-height:20px}
.main-nav{position:absolute;right:130px;top:54px;display:flex;gap:39px;font-size:14px;font-weight:700;color:var(--cyan)}
.main-nav .current{color:var(--blue)}
.nav-marker{position:absolute;left:754px;top:74px;width:0;height:0;border-left:6px solid transparent;border-right:6px solid transparent;border-bottom:6px solid var(--cyan)}

.sub-nav{position:absolute;left:0;top:80px;width:1200px;height:40px;background:var(--cyan);box-shadow:inset 0 3px 3px rgba(0,0,0,.12)}
.sub-nav ul{position:absolute;right:130px;top:14px;display:flex;gap:17px;list-style:none;font-size:12px;color:var(--white)}

.hero{position:absolute;left:0;top:120px;width:1200px;height:280px;background:linear-gradient(180deg,#5c7e92 0%,#8fa6b2 30%,#c9d3d6 55%,#d9dedd 75%,#cfd4d2 100%)}
.hero-headline{position:absolute;left:128px;top:32px;font-family:"Roboto Condensed",Arial,sans-serif;font-weight:400;font-size:36px;line-height:43px;color:var(--white);text-shadow:1px 2px 4px rgba(0,0,0,.55);letter-spacing:-0.6px}
.hero-arrow{position:absolute;top:115px;width:50px;height:50px;background:rgba(40,40,40,.65)}
.hero-arrow.prev{left:0}
.hero-arrow.next{right:0}
.hero-dots{position:absolute;left:1035px;top:251px;display:flex;gap:5px}
.hero-dots span{width:8px;height:8px;background:var(--white)}
.hero-dots .active{background:var(--cyan)}

.intro{position:absolute;left:130px;top:428px;width:620px;font-size:12px;line-height:14px}
.intro p{margin-bottom:8px}
.intro .hl{color:var(--cyan);font-weight:700}
.intro .lead{color:var(--cyan);font-weight:700;margin-top:1px}

.calc-link{position:absolute;left:770px;top:430px;width:300px;height:68px}
.calc-icon{position:absolute;left:0;top:0;width:68px;height:68px;border-radius:50%;background:var(--cyan)}
.calc-text{position:absolute;left:79px;top:14px;font-size:14px;line-height:17px;font-weight:700;color:var(--cyan)}

.services{position:absolute;left:130px;top:552px;display:flex;gap:20px}
.service{width:220px}
.service h3{font-size:14px;font-weight:700;color:var(--blue);height:25px;border-bottom:2px solid var(--blue);display:flex;align-items:flex-start;gap:9px}
.service h3 svg{margin-top:3px}
.service ul{list-style:none;font-size:12px;line-height:21px;margin-top:4px}
.service .group{font-weight:700;color:#000}

.panel{position:absolute;left:130px;top:688px;width:620px;font-size:12px;line-height:14px}
.panel .cta{color:var(--cyan);font-weight:700;margin-top:7px}
.accreditation{position:absolute;left:770px;top:688px;width:300px}
.accreditation h4{font-size:12px;font-weight:700;color:var(--cyan)}
.badge{position:absolute;top:32px;width:98px;height:26px;background:var(--badge);border-radius:3px}

.site-footer{position:absolute;left:130px;top:900px;width:940px;border-top:1px solid var(--rule);padding-top:13px;font-size:11px;line-height:20px;color:var(--ink)}
.social{position:absolute;right:0;top:20px;display:flex;gap:14px}
.social span{width:25px;height:25px;border-radius:50%;background:var(--cyan)}
</style>
</head>
<body>
<div class="page">
  <header class="site-header">
    <a class="brand" href="#">
      <span class="brand-mark"></span>
      <span class="brand-name">brightwell lending</span>
    </a>
    <nav class="main-nav">
      <a class="current" href="#">Home</a>
      <a href="#">Services</a>
      <a href="#">About Us</a>
      <a href="#">FAQ</a>
      <a href="#">Contact Us</a>
    </nav>
    <span class="nav-marker"></span>
  </header>

  <nav class="sub-nav">
    <ul>
      <li>&gt; Home loans</li>
      <li>&gt; Investment loans</li>
      <li>&gt; Refinancing loans</li>
      <li>&gt; Business loans</li>
    </ul>
  </nav>

  <section class="hero" role="img" aria-label="Photo of two children playing at the edge of the sea">
    <h1 class="hero-headline">Brightwell Lending finds the right<br>loan for our customers.</h1>
    <a class="hero-arrow prev" href="#" aria-label="Previous slide">
      <svg width="50" height="50" viewBox="0 0 50 50"><path d="M31 12 L19 25 L31 38" fill="none" stroke="#fff" stroke-width="4"/></svg>
    </a>
    <a class="hero-arrow next" href="#" aria-label="Next slide">
      <svg width="50" height="50" viewBox="0 0 50 50"><path d="M19 12 L31 25 L19 38" fill="none" stroke="#fff" stroke-width="4"/></svg>
    </a>
    <div class="hero-dots"><span class="active"></span><span></span><span></span></div>
  </section>

  <section class="intro">
    <p>At <span class="hl">Brightwell Lending</span> we work hard to find the right loan for our customers. We do that because we are backed by sound industry knowledge, professional experience and a great customer service approach. Brightwell Lending guarantees that we will always tailor the best solution for your individual lending needs.</p>
    <p>We can do that because we have access to a wide variety of lending options from major banks to non-bank lenders and we are committed to finding the right lending product for you.</p>
    <p class="lead">We offer a unique approach to help you find the right:</p>
  </section>

  <a class="calc-link" href="#">
    <span class="calc-icon">
      <svg width="68" height="68" viewBox="0 0 68 68">
        <rect x="24" y="20" width="20" height="27" rx="2" fill="none" stroke="#fff" stroke-width="2"/>
        <rect x="28" y="24" width="12" height="5" fill="#fff"/>
        <g fill="#fff">
          <rect x="28" y="32" width="3" height="3"/><rect x="32.5" y="32" width="3" height="3"/><rect x="37" y="32" width="3" height="3"/>
          <rect x="28" y="37" width="3" height="3"/><rect x="32.5" y="37" width="3" height="3"/><rect x="37" y="37" width="3" height="3"/>
          <rect x="28" y="42" width="3" height="2"/><rect x="32.5" y="42" width="3" height="2"/><rect x="37" y="42" width="3" height="2"/>
        </g>
      </svg>
    </span>
    <span class="calc-text">Find out how much you could<br>borrow
      <svg width="18" height="12" viewBox="0 0 18 12" style="margin-left:6px"><path d="M2 1 L7 6 L2 11 M9 1 L14 6 L9 11" fill="none" stroke="#2EADE3" stroke-width="2.4"/></svg>
    </span>
  </a>

  <section class="services">
    <article class="service">
      <h3><svg width="10" height="10" viewBox="0 0 10 10"><path d="M1 1 L8 8 M8 3 V8 H3" fill="none" stroke="#004B70" stroke-width="2.4"/></svg>Home Loan</h3>
      <ul><li>- Home buyers</li><li>- First home buyers</li><li>- Over 20 lenders</li></ul>
    </article>
    <article class="service">
      <h3><svg width="10" height="10" viewBox="0 0 10 10"><path d="M1 1 L8 8 M8 3 V8 H3" fill="none" stroke="#004B70" stroke-width="2.4"/></svg>Investment Loan</h3>
      <ul><li>- Property investment loans</li><li>- Interest only loans</li></ul>
    </article>
    <article class="service">
      <h3><svg width="10" height="10" viewBox="0 0 10 10"><path d="M1 1 L8 8 M8 3 V8 H3" fill="none" stroke="#004B70" stroke-width="2.4"/></svg>Refinancing</h3>
      <ul><li>- Refinancing for the best rate</li><li>- Upsizing or downsizing</li><li>- Change from a variable to a fixed rate</li></ul>
    </article>
    <article class="service">
      <h3><svg width="10" height="10" viewBox="0 0 10 10"><path d="M1 1 L8 8 M8 3 V8 H3" fill="none" stroke="#004B70" stroke-width="2.4"/></svg>Business Loan</h3>
      <ul><li class="group">Business Finance</li><li>- Long term</li><li>- Short term</li><li>- Equipment and Leasing</li></ul>
    </article>
  </section>

  <section class="panel">
    <p>There are many different loan products in the marketplace. Brightwell Lending has access to a wide panel of lenders which means we can access bank and non-bank lenders that meet the individual needs of our customers.</p>
    <p class="cta">Contact Brightwell Lending today on: 1800 555 014 to find out more.</p>
  </section>

  <section class="accreditation">
    <h4>Accreditation logos</h4>
    <span class="badge" style="left:0" aria-label="Accreditation badge"></span>
    <span class="badge" style="left:160px" aria-label="Accreditation badge"></span>
  </section>

  <footer class="site-footer">
    <p>Terms of Use | Legal notice | Sitemap | Disclaimer</p>
    <p>Copyright © 2012 Brightwell Lending.&nbsp; All rights reserved.</p>
    <div class="social" aria-label="Social links"><span></span><span></span><span></span><span></span></div>
  </footer>
</div>
</body>
</html>
```